An expert for Professional and Technical Evaluation of Painting Work Needs a New Letterhead Design

I own a mid-sized painting company and also work as an expert for professional and technical evaluation of painting work in the area of Zurich.

Please read the project description and the must-have-requirements carefully!

I attached 1 PDF which will help you create a new letterhead design:

THE NEW DESIGN DOESN'T NEED A LOGO! (Because it won't represent a company, it represents only a service)
Updates

Dear designers We had a discussion about the location/placement of the design and came to the conclusion that we only want the design to be in the header area of the A4-paper. We would be glad to receive some revised version of your designs. Thank you and kind regards!

Project Deadline Extended
Reason: Due to the fact that only 20% of the designer have understood the brief and submitted designs that have met the requirements we decided to extend the contest deadline.

Project Deadline Extended
Reason: A great deal of good designs were submitted in the last few days. A big thank you to all the participating designers for your good work. We need a few more days to discuss some changes with certain designers and to decide which design will win.

Target Market(s)

(Insurance) Companies, partly also private clients.

Industry/Entity Type

Painting

Colors

Designer to choose colors to be used in the design.

Requirements
Must have
• All information (text, phone numbers, ...) of the old design ("old_letterhead_design.pdf") has also to be in the new one. Additional to that there are a few changes:
The phone numbers "01 583 61 47" and "01 583 61 37" change to "044 583 61 47" and "044 583 61 37". And please mention also this email address: gutachten@valmorkeller.example .

- The design should only be in the header-area of the A4-paper. An the background color of the A4-paper will be white.

- The design should consist of two designs. One for the first page and a smaller version of the design for the following pages.

- THE NEW DESIGN DOESN'T NEED A LOGO! You can make a design with geometric forms, ...

- The new design should have a juridical look. It should only contain colors like brown, fawn, black, light green, ...... colors which look serious/reliable.
Nice to have
• Geometric Forms, Symbols or other design elements.

- It would also be nice to have some design elements which emphasize the kind of work we are offering.

```html
<!DOCTYPE html>
<html lang="en">
<head>
<meta charset="utf-8">
<title>Letterhead – Valmor Keller, eidg.dipl. Malermeister</title>
<link rel="stylesheet" href="https://fonts.googleapis.com/css2?family=Source+Sans+3:wght@400;600;700&display=swap">
<style>
  :root {
    --backdrop: #e9e7e3;
    --paper: #ffffff;
    --ink: #1d1d1d;
    --ink-soft: #444444;
    --rule: #d7d7d7;
    --header-shade: #f1f1f1;
    --art-espresso: #3b2a1e;
    --art-brown: #6e4b2e;
    --art-fawn: #c8a678;
    --art-sand: #e3d3b4;
    --art-sage: #a9c08a;
    --art-green: #7f9f5c;
    --facet-grey: #ececec;
  }
  * { box-sizing: border-box; margin: 0; padding: 0; }
  html, body { width: 1200px; height: 840px; overflow: hidden; }
  body {
    background: var(--backdrop);
    font-family: "Source Sans 3", "Myriad Pro", Arial, sans-serif;
    color: var(--ink);
    position: relative;
  }
  .sheet {
    position: absolute;
    top: 30px;
    width: 552px;
    height: 780px;
    background: var(--paper);
    box-shadow: 0 4px 14px rgba(0,0,0,.18);
    overflow: hidden;
  }
  .sheet--first { left: 36px; }
  .sheet--following { left: 612px; }

  /* header */
  .letterhead {
    position: absolute; left: 0; top: 0; width: 100%;
    background: linear-gradient(180deg, var(--paper) 0%, var(--header-shade) 100%);
    border-bottom: 1px solid var(--rule);
    box-shadow: 0 3px 6px rgba(0,0,0,.08);
  }
  .sheet--first .letterhead { height: 172px; }
  .sheet--following .letterhead { height: 124px; }

  .letterhead__art {
    position: absolute; left: 0; top: 0;
    background: linear-gradient(100deg, var(--art-espresso) 0%, var(--art-brown) 26%, var(--art-fawn) 50%, var(--art-sand) 68%, var(--art-sage) 84%, var(--art-green) 100%);
  }
  .sheet--first .letterhead__art { width: 330px; height: 96px; }
  .sheet--following .letterhead__art { width: 250px; height: 66px; }

  .sender {
    position: absolute; right: 16px; text-align: right; line-height: 1.35;
    font-style: normal; color: var(--ink);
  }
  .sheet--first .sender { top: 100px; font-size: 8.5px; }
  .sheet--following .sender { top: 68px; font-size: 7.5px; }
  .sender__name { font-weight: 700; }
  .sender__title { font-weight: 600; }
  .sheet--first .sender__headline { font-size: 12.5px; }
  .sheet--following .sender__headline { font-size: 10.5px; }
  .sender__divider { margin: 0 5px; font-weight: 400; color: var(--art-brown); }

  .services {
    position: absolute; left: 14px; right: 14px;
    display: flex; justify-content: space-between;
    list-style: none;
    text-transform: uppercase;
    letter-spacing: .04em;
    color: var(--ink);
    white-space: nowrap;
  }
  .services li::before {
    content: ""; display: inline-block;
    width: 6px; height: 6px; border-radius: 50%;
    background: var(--ink); margin-right: 4px; vertical-align: 1px;
  }
  .sheet--first .services { bottom: 6px; font-size: 9.5px; }
  .sheet--following .services { bottom: 6px; font-size: 8px; }
  .sheet--following .services li::before { width: 5px; height: 5px; }

  /* facet background */
  .facets {
    position: absolute; left: 0; right: 0; bottom: 0; height: 360px;
    background: radial-gradient(ellipse at 40% 60%, var(--facet-grey) 0%, rgba(236,236,236,0) 70%);
  }

  /* letter body */
  .letter {
    position: absolute; left: 62px; right: 56px;
    font-size: 11px; line-height: 1.45; color: var(--ink-soft);
  }
  .sheet--first .letter { top: 204px; }
  .sheet--following .letter { top: 156px; font-size: 12px; }
  .letter__recipient { margin: 12px 0 16px; }
  .letter p { margin-bottom: 8px; }
  .letter__closing { margin-top: 14px; }
  .signature {
    display: block; width: 120px; height: 34px; margin: 10px 0 4px;
    background: linear-gradient(90deg, rgba(60,60,60,.15), rgba(60,60,60,.35), rgba(60,60,60,.1));
    border-radius: 20px;
  }
</style>
</head>
<body>

<section class="sheet sheet--first" aria-label="First page letterhead">
  <header class="letterhead">
    <div class="letterhead__art" role="img" aria-label="Cluster of overlapping translucent cubes and paint bands in brown, fawn and light green"></div>
    <address class="sender">
      <div class="sender__headline"><span class="sender__name">Valmor Keller</span><span class="sender__divider">|</span><span class="sender__title">eidg.dipl. Malermeister</span></div>
      <div>Lindenweg 7 | 8804 Au</div>
      <div>Telefon 044 583 61 47 | Fax 044 583 61 37</div>
      <div>gutachten@valmorkeller.example</div>
    </address>
    <ul class="services">
      <li>Gutachten</li><li>Expertisen</li><li>Devisierungen</li><li>Farbberatungen</li><li>Dekorative Gestaltungen</li>
    </ul>
  </header>
  <div class="facets" role="img" aria-label="Faint grey pattern of overlapping translucent squares"></div>
  <article class="letter">
    <div>November 1, 2012</div>
    <div class="letter__recipient">Mr. Oren Ashby<br>56 Quarry Row<br>Ashford, U.K 54321</div>
    <p>Dear Mr. Ashby</p>
    <p>The first paragraph of a typical business letter is used to state the main point of the letter. Begin with a friendly opening; then quickly transition into the purpose of your letter. Use a couple of sentences to explain the purpose, but do not go in to detail until the next paragraph.</p>
    <p>Beginning with the second paragraph, state the supporting details to justify your purpose. These may take the form of background information, statistics or first-hand accounts. A few short paragraphs within the body of the letter should be enough to support your reasoning.</p>
    <p>Finally, in the closing paragraph, briefly restate your purpose and why it is important. If the purpose of your letter is employment related, consider ending your letter with your contact information. However, if the purpose is informational, think about closing with gratitude for the reader's time.</p>
    <div class="letter__closing">Sincerely,</div>
    <span class="signature" role="img" aria-label="Handwritten signature of Mara Quill"></span>
    <div>President</div>
  </article>
</section>

<section class="sheet sheet--following" aria-label="Following page letterhead">
  <header class="letterhead">
    <div class="letterhead__art" role="img" aria-label="Cluster of overlapping translucent cubes and paint bands in brown, fawn and light green"></div>
    <address class="sender">
      <div class="sender__headline"><span class="sender__name">Valmor Keller</span><span class="sender__divider">|</span><span class="sender__title">eidg.dipl. Malermeister</span></div>
      <div>Lindenweg 7 | 8804 Au</div>
      <div>Telefon 044 583 61 47 | Fax 044 583 61 37</div>
    </address>
    <ul class="services">
      <li>Gutachten</li><li>Expertisen</li><li>Devisierungen</li><li>Farbberatungen</li><li>Dekorative Gestaltungen</li>
    </ul>
  </header>
  <div class="facets" role="img" aria-label="Faint grey pattern of overlapping translucent squares"></div>
  <article class="letter">
    <div>November 1, 2012</div>
    <div class="letter__recipient">Mr. Oren Ashby<br>56 Quarry Row<br>Ashford, U.K 54321</div>
    <p>Dear Mr. Ashby</p>
    <p>The first paragraph of a typical business letter is used to state the main point of the letter. Begin with a friendly opening; then quickly transition into the purpose of your letter. Use a couple of sentences to explain the purpose, but do not go in to detail until the next paragraph.</p>
  </article>
</section>

</body>
</html>
```